Book Title: THE QUIET LEDGER
Book Sub Title: Notes on forgotten harbours and the keepers who tended their lamps
Vibe: Professional, stylish, trustworthy (high-end men's fashion)
Website (for inspiration): www.velmorandpike.com
Attached: a potential photo to use for the cover, but open to other options (from our website)

```html
<!DOCTYPE html>
<html lang="en">
<head>
<meta charset="utf-8">
<title>The Quiet Ledger – Book Cover</title>
<link rel="stylesheet" href="https://fonts.googleapis.com/css2?family=Oswald:wght@600;700&family=Didact+Gothic&family=Montserrat:wght@500;700&display=swap">
<style>
  :root {
    --ink-navy: #1c1f33;
    --gold: #c0a676;
    --slate: #4a5563;
    --paper: #ffffff;
    --body-ink: #1a1a1a;
    --floor-light: #efe6da;
    --floor-mid: #d9c8b3;
  }
  * { margin: 0; padding: 0; box-sizing: border-box; }
  html, body { width: 1200px; height: 864px; overflow: hidden; background: var(--paper); }
  .cover-spread { position: relative; width: 1200px; height: 864px; background: var(--paper); overflow: hidden; }

  /* Back cover */
  .back-cover { position: absolute; left: 0; top: 0; width: 576px; height: 864px; }
  .back-floor {
    position: absolute; left: 300px; top: 550px; width: 276px; height: 314px;
    background: radial-gradient(ellipse at 100% 60%, var(--floor-light) 0%, rgba(239,230,218,0.5) 45%, rgba(255,255,255,0) 75%);
  }
  .back-blurb {
    position: absolute; left: 68px; top: 86px; width: 449px;
    font-family: "Didact Gothic", sans-serif; font-size: 13.2px; line-height: 16px;
    color: var(--body-ink); text-align: justify; hyphens: auto; letter-spacing: 0.15px;
  }
  .barcode-area { position: absolute; left: 357px; top: 749px; width: 160px; height: 88px; background: var(--paper); border: 1px solid #111; }

  /* Spine */
  .spine { position: absolute; left: 576px; top: 0; width: 48px; height: 864px; background: var(--ink-navy); }
  .spine-title, .spine-author {
    position: absolute; left: 50%; color: var(--paper); font-family: "Oswald", sans-serif; font-weight: 600;
    white-space: nowrap; transform-origin: left center;
  }
  .spine-title { top: 124px; font-size: 38px; line-height: 1; transform: translate(13px, 0) rotate(90deg); }
  .spine-author { top: 603px; font-size: 23px; line-height: 1; color: var(--paper); transform: translate(9px, 0) rotate(90deg); }

  /* Front cover */
  .front-cover { position: absolute; left: 624px; top: 0; width: 576px; height: 864px; background: var(--paper); }
  .front-title { position: absolute; left: 0; top: 64px; width: 576px; text-align: center; font-family: "Oswald", sans-serif; font-weight: 700; line-height: 0.95; }
  .front-title .title-top { display: block; font-size: 92px; color: var(--ink-navy); letter-spacing: 1px; }
  .front-title .title-bottom { display: block; font-size: 116px; color: var(--gold); letter-spacing: 2px; margin-top: 2px; }
  .subtitle-rule { position: absolute; left: 130px; width: 316px; height: 2px; background: linear-gradient(90deg, rgba(74,85,99,0), var(--slate) 20%, var(--slate) 80%, rgba(74,85,99,0)); }
  .subtitle-rule.top { top: 259px; }
  .subtitle-rule.bottom { top: 313px; height: 1px; }
  .front-subtitle {
    position: absolute; left: 0; top: 264px; width: 576px; text-align: center;
    font-family: "Montserrat", sans-serif; font-weight: 700; font-size: 15.5px; line-height: 22px; color: var(--slate); letter-spacing: 0.3px;
  }
  .front-subtitle .accent { color: var(--gold); }
  .cover-photo {
    position: absolute; left: 0; top: 318px; width: 576px; height: 450px;
    background:
      linear-gradient(180deg, rgba(255,255,255,0) 70%, var(--paper) 100%),
      linear-gradient(180deg, var(--paper) 0%, #f6f6f6 38%, var(--floor-light) 58%, var(--floor-mid) 72%, var(--floor-light) 100%);
  }
  .author-name { position: absolute; left: 0; top: 754px; width: 576px; text-align: center; font-family: "Oswald", sans-serif; font-weight: 700; font-size: 62px; line-height: 1; color: var(--ink-navy); letter-spacing: 0.5px; }
  .author-accolade { position: absolute; left: 0; top: 816px; width: 576px; text-align: center; font-family: "Didact Gothic", sans-serif; font-size: 13px; color: var(--slate); letter-spacing: 0.5px; }
  .author-accolade strong { font-family: "Montserrat", sans-serif; font-weight: 700; color: var(--slate); }
</style>
</head>
<body>
<main class="cover-spread">
  <section class="back-cover">
    <div class="back-floor" aria-hidden="true"></div>
    <p class="back-blurb">Lorem ipsum dolor sit amet, consectetur adipisicing elit, sed do eiusmod tempor incididunt ut labore et dolore magna aliqua. Ut enim ad minim veniam, quis nostrud exercitation ullamco laboris nisi ut aliquip ex ea commodo consequat. Duis aute irure dolor in reprehenderit in voluptate velit esse cillum dolore eu fugiat nulla pariatur. Excepteur sint occaecat cupidatat non proident, sunt in culpa qui officia deserunt mollit anim id est laborum. Sed ut perspiciatis unde omnis iste natus error sit voluptatem accusantium doloremque laudantium, totam rem aperiam, eaque ipsa quae ab illo inventore veritatis et quasi architecto beatae vitae dicta sunt explicabo. Nemo enim ipsam voluptatem quia voluptas sit aspernatur aut odit aut fugit, sed quia consequuntur magni dolores eos qui ratione voluptatem sequi nesciunt. Neque porro quisquam est, qui dolorem ipsum quia dolor sit amet, consectetur, adipisci velit, sed quia non numquam eius modi tempora incidunt ut labore et dolore magnam aliquam quaerat voluptatem.<br>Lorem ipsum dolor sit amet, consectetur adipisicing elit, sed do eiusmod tempor incididunt ut labore et dolore magna aliqua. Ut enim ad minim veniam, quis nostrud exercitation ullamco laboris nisi ut aliquip ex ea commodo consequat. Duis aute irure dolor in reprehenderit in voluptate velit esse cillum dolore eu fugiat nulla pariatur. Excepteur sint occaecat cupidatat non proident, sunt in culpa qui officia deserunt mollit anim id est laborum. Sed ut perspiciatis unde omnis iste natus error sit voluptatem accusantium doloremque laudantium, totam rem aperiam, eaque ipsa quae ab illo inventore veritatis et quasi architecto beatae vitae dicta sunt explicabo. Nemo enim ipsam voluptatem quia voluptas sit aspernatur aut odit aut fugit, sed quia consequuntur magni dolores eos qui ratione voluptatem sequi nesciunt. Neque porro quisquam est, qui dolorem ipsum quia dolor sit amet, consectetur, adipisci velit, sed quia non numquam eius modi tempora incidunt ut labore et dolore magnam aliquam quaerat voluptatem.</p>
    <div class="barcode-area" aria-hidden="true"></div>
  </section>

  <section class="spine">
    <span class="spine-title">THE QUIET LEDGER</span>
    <span class="spine-author">OWEN MARLOWE</span>
  </section>

  <section class="front-cover">
    <h1 class="front-title">
      <span class="title-top">THE QUIET</span>
      <span class="title-bottom">LEDGER</span>
    </h1>
    <div class="subtitle-rule top"></div>
    <p class="front-subtitle">Notes on forgotten harbours and the keepers<br>who tended <span class="accent">their lamps</span></p>
    <div class="subtitle-rule bottom"></div>
    <div class="cover-photo" role="img" aria-label="Photograph of the author in a navy suit seated on a wooden stool beside a clothing rail of jackets, shirts and coats on a pale wood floor"></div>
    <p class="author-name">OWEN MARLOWE</p>
    <p class="author-accolade">“Best Dressed Man In America” by <strong>Halden Review</strong></p>
  </section>
</main>
</body>
</html>
```